Business Card Design

We are a commercial real estate brokerage in San Francisco, leasing office buildings downtown.
I would like a clean, elegant look. Simple but powerful .

Industry/Entity Type

Business

Contact Information for Business Card

Derek Hollings
lic# 02875140
415.287.6041
derek@vexa-commercial.com
vexa-commercial.com

```html
<!DOCTYPE html>
<html lang="en">
<head>
<meta charset="utf-8">
<title>Vexa Commercial – Business Card</title>
<link href="https://fonts.googleapis.com/css2?family=Jost:wght@400;500;600&display=swap" rel="stylesheet">
<style>
  :root {
    --page-bg: #e9e6e2;
    --card-bg: #ffffff;
    --slate: #6f82a3;
    --ink: #3c3c3c;
    --ink-soft: #6a6a6a;
  }
  html, body {
    margin: 0;
    padding: 0;
    width: 1200px;
    height: 900px;
    overflow: hidden;
    background: var(--page-bg);
    font-family: "Jost", "Century Gothic", sans-serif;
  }
  .card {
    position: absolute;
    left: 100px;
    top: 164px;
    width: 1000px;
    height: 572px;
    background: var(--card-bg);
    box-shadow: 0 6px 22px rgba(0,0,0,0.18);
    overflow: hidden;
  }
  .brand {
    position: absolute;
    left: 120px;
    top: 82px;
    display: flex;
    align-items: center;
    gap: 18px;
  }
  .brand-mark {
    width: 22px;
    height: 22px;
    background: var(--slate);
  }
  .brand-name {
    margin: 0;
    font-weight: 500;
    font-size: 54px;
    letter-spacing: 1px;
    line-height: 1;
    color: var(--slate);
    text-transform: uppercase;
  }
  .accent-block {
    position: absolute;
    left: 0;
    top: 218px;
    width: 64px;
    height: 56px;
    background: var(--slate);
  }
  .agent {
    position: absolute;
    left: 98px;
    top: 222px;
  }
  .agent-name {
    margin: 0;
    font-weight: 600;
    font-size: 24px;
    letter-spacing: 0.5px;
    color: var(--ink);
    text-transform: uppercase;
  }
  .agent-license {
    margin: 4px 0 0;
    font-size: 21px;
    color: var(--ink-soft);
  }
  .contact {
    position: absolute;
    left: 64px;
    top: 330px;
    margin: 0;
    padding: 0;
    list-style: none;
  }
  .contact-item {
    display: flex;
    align-items: center;
    gap: 16px;
    height: 40px;
    font-size: 24px;
    color: var(--ink-soft);
  }
  .contact-icon {
    width: 20px;
    height: 20px;
    flex: none;
  }
</style>
</head>
<body>
  <article class="card">
    <header class="brand">
      <span class="brand-mark"></span>
      <h1 class="brand-name">Vexa Commercial</h1>
    </header>

    <div class="accent-block"></div>

    <section class="agent">
      <h2 class="agent-name">Derek Hollings</h2>
      <p class="agent-license">lic# 02875140</p>
    </section>

    <ul class="contact">
      <li class="contact-item">
        <svg class="contact-icon" viewBox="0 0 20 20" aria-hidden="true">
          <path d="M5 2 h3 l1 4 -2 1.5 c1 2.5 3 4.5 5.5 5.5 L14 11 l4 1 v3 c0 1.5 -1 2 -2 2 C9 17 3 11 3 4 3 3 3.5 2 5 2z" fill="var(--slate)"/>
        </svg>
        <span>415.287.6041</span>
      </li>
      <li class="contact-item">
        <svg class="contact-icon" viewBox="0 0 20 20" aria-hidden="true">
          <rect x="2" y="5" width="16" height="11" fill="var(--slate)"/>
          <path d="M2 5 L10 11 L18 5" fill="none" stroke="#fff" stroke-width="1.4"/>
        </svg>
        <span>derek@vexa-commercial.com</span>
      </li>
      <li class="contact-item">
        <svg class="contact-icon" viewBox="0 0 20 20" aria-hidden="true">
          <g fill="none" stroke="var(--slate)" stroke-width="1.4">
            <circle cx="10" cy="10" r="8"/>
            <ellipse cx="10" cy="10" rx="3.5" ry="8"/>
            <line x1="2" y1="10" x2="18" y2="10"/>
            <line x1="3.5" y1="6" x2="16.5" y2="6"/>
            <line x1="3.5" y1="14" x2="16.5" y2="14"/>
          </g>
        </svg>
        <span>vexa-commercial.com</span>
      </li>
    </ul>
  </article>
</body>
</html>
```